Floristry Business Card Design Project

I have a logo now and am looking to incorporate this into a business card. I would like a double sided business card. I would like one side to be decorative so that it blends well when included with floral arrangements and that can also be used as the front of a card and the other side will contain the business details. The font on the business details side should be clear although some decorative font would be ok. I have included the logo files for use in the business card design.

Feel free to break up the logo and use certain aspects of it in the design. Really looking for something that stands out and that is really creative.

Industry/Entity Type

Floral

Requirements
Should not have
• Nothing tacky or corny. The logo should be clearly read (perhaps a background colour).

```html
<!DOCTYPE html>
<html lang="en">
<head>
<meta charset="utf-8">
<title>Meadow Bloom business cards</title>
<link href="https://fonts.googleapis.com/css2?family=Crimson+Text:wght@400;600;700&display=swap" rel="stylesheet">
<style>
  :root {
    --backdrop: #e6e9e6;
    --card-white: #ffffff;
    --sage: #7dbb93;
    --sage-deep: #4f9468;
    --brand-green: #3f8a4f;
    --grass-light: #8ccf5a;
    --grass-mid: #4f9a2e;
    --grass-dark: #2c5e1c;
    --ink: #3a3a3a;
    --blossom: #d9785e;
  }
  * { box-sizing: border-box; margin: 0; padding: 0; }
  html, body { width: 1200px; height: 1000px; overflow: hidden; }
  body {
    background: var(--backdrop);
    font-family: "Crimson Text", Georgia, serif;
    position: relative;
  }
  .card {
    position: absolute;
    left: 240px;
    width: 720px;
    height: 410px;
    border-radius: 24px;
    overflow: hidden;
    background: var(--card-white);
    box-shadow: 0 10px 28px rgba(0,0,0,0.18);
  }
  .card--details { top: 70px; }
  .card--brand { top: 520px; }

  /* details side */
  .meadow-strip {
    position: absolute; left: 0; top: 0; width: 100%; height: 120px;
    background: linear-gradient(100deg, var(--grass-dark) 0%, var(--grass-mid) 45%, var(--grass-light) 100%);
  }
  .name-band {
    position: absolute; left: 0; top: 120px; width: 100%; height: 96px;
    background: var(--sage);
    border-top: 5px solid var(--card-white);
    padding: 18px 0 0 80px;
    color: var(--card-white);
  }
  .name-band__name { font-size: 30px; font-weight: 700; line-height: 1.05; }
  .name-band__role { font-size: 22px; font-weight: 400; }
  .contact {
    position: absolute; left: 110px; top: 250px;
    color: var(--ink); font-size: 21px; line-height: 1.3;
  }
  .web-line {
    position: absolute; left: 80px; bottom: 40px;
    display: flex; align-items: center; gap: 14px;
    color: var(--ink); font-size: 22px;
  }
  .web-line__dot { width: 18px; height: 18px; border-radius: 50%; border: 2px solid var(--blossom); }

  /* brand side */
  .meadow-field {
    position: absolute; inset: 0;
    background: linear-gradient(160deg, var(--grass-light) 0%, var(--grass-mid) 55%, var(--grass-dark) 100%);
  }
  .brand-panel {
    position: absolute; left: 200px; top: 40px; width: 340px; height: 280px;
    background: var(--card-white);
    border-radius: 22px;
    border: 3px solid var(--brand-green);
    outline: 3px solid var(--card-white);
    display: flex; flex-direction: column; align-items: center;
    padding-top: 22px;
  }
  .wreath {
    width: 180px; height: 180px; border-radius: 50%;
    background: radial-gradient(circle, #ffffff 0 52%, #cfe6c4 56%, #e9b3a4 70%, #bcd9a8 82%, #ffffff 90%);
  }
  .brand-name {
    margin-top: 16px;
    color: var(--brand-green);
    font-size: 30px; font-weight: 600;
    letter-spacing: 4px; text-transform: uppercase;
  }
  .brand-web {
    position: absolute; left: 0; width: 100%; top: 344px;
    text-align: center; color: var(--card-white);
    font-size: 22px; letter-spacing: 2px;
  }
</style>
</head>
<body>
  <section class="card card--details">
    <div class="meadow-strip" role="img" aria-label="Photograph of white daisies in green grass"></div>
    <div class="name-band">
      <p class="name-band__name">Rowan Ellery</p>
      <p class="name-band__role">Managing Director</p>
    </div>
    <div class="contact">
      <p>001 555 01842</p>
      <p>rowan@meadowbloom.com</p>
    </div>
    <div class="web-line">
      <span class="web-line__dot"></span>
      <span>www.MeadowBloom.com</span>
    </div>
  </section>

  <section class="card card--brand">
    <div class="meadow-field" role="img" aria-label="Photograph of a meadow with daisies and dandelions"></div>
    <div class="brand-panel">
      <div class="wreath" role="img" aria-label="Circular floral wreath ornament"></div>
      <p class="brand-name">Meadow Bloom</p>
    </div>
    <p class="brand-web">www.MeadowBloom.com</p>
  </section>
</body>
</html>
```